Letterhead

Can you please design me a letterhead that I can use electronically in word as a template. I have attached my business card as I would like the design to reflect this logo.

```html
<!DOCTYPE html>
<html lang="en">
<head>
<meta charset="utf-8">
<title>Corvell Letterhead</title>
<link rel="stylesheet" href="https://fonts.googleapis.com/css2?family=Arimo:wght@400;700&display=swap">
<style>
  :root {
    --brand-red: #a5202f;
    --band-black: #141414;
    --ink-dark: #2b1a1c;
    --paper: #ffffff;
  }
  html, body {
    margin: 0;
    padding: 0;
    background: var(--paper);
    overflow: hidden;
  }
  .letterhead {
    position: relative;
    width: 899px;
    height: 1200px;
    overflow: hidden;
    background: var(--paper);
    font-family: "Arimo", Arial, sans-serif;
  }
  .brand-name {
    position: absolute;
    left: 50px;
    top: -8px;
    margin: 0;
    font-size: 78px;
    font-weight: 700;
    line-height: 1;
    letter-spacing: 1px;
    color: var(--brand-red);
  }
  .header-band {
    position: absolute;
    left: 7px;
    top: 78px;
    width: 884px;
    height: 44px;
  }
  .header-band svg { display: block; }
  .tagline {
    position: absolute;
    left: 137px;
    top: 91px;
    margin: 0;
    font-size: 16px;
    font-weight: 700;
    color: var(--ink-dark);
    line-height: 1;
  }
  .footer-wave {
    position: absolute;
    left: 0;
    top: 1110px;
    width: 899px;
    height: 90px;
  }
  .footer-wave svg { display: block; }
  .signatory, .contact {
    position: absolute;
    margin: 0;
    font-size: 16px;
    line-height: 20px;
    color: var(--ink-dark);
  }
  .signatory { left: 17px; top: 1156px; }
  .contact { right: 22px; top: 1145px; text-align: right; }
</style>
</head>
<body>
<div class="letterhead">
  <h1 class="brand-name">corvell</h1>

  <div class="header-band">
    <svg width="884" height="44" viewBox="0 0 884 44">
      <rect x="0" y="0" width="884" height="44" fill="var(--brand-red)"/>
      <rect x="0" y="0" width="128" height="44" fill="var(--band-black)"/>
      <rect x="855" y="0" width="4" height="44" fill="var(--band-black)"/>
      <rect x="863" y="0" width="4" height="44" fill="var(--band-black)"/>
      <rect x="871" y="0" width="4" height="44" fill="var(--band-black)"/>
      <rect x="879" y="0" width="5" height="44" fill="var(--band-black)"/>
    </svg>
  </div>
  <p class="tagline">Business Consultants Pvt Ltd</p>

  <div class="footer-wave">
    <svg width="899" height="90" viewBox="0 0 899 90">
      <path d="M0 22 C 120 36, 260 42, 420 30 C 600 14, 760 4, 899 8 L 899 90 L 0 90 Z" fill="var(--brand-red)"/>
    </svg>
  </div>

  <p class="signatory">Helena Marsh<br>Principal</p>
  <p class="contact">Hello: 0400-555123<br>E-mail: helena@corvell.net.au</p>
</div>
</body>
</html>
```